I need a Label design for my copper 71 kombucha brand that is launching soon

I want a label to go on my copper 71 kombucha bottle.
I have a logo image uploaded in the files but I am open to changes to this logo or even a completely New one if you think you can do better. This logo is based on the idea of an s-shaped naga. I particularly like the nagas from temples in luang prabang.
I also want to include the slogan - dare to be delicious.
The label should be some kind of oval at 80mm high by 70mm wide.
The label will go on a clear glass bottle. The kombucha will be visible and comes in different shades of red,yellow and purple.
The word kombucha should be clearly visible.
i want a very colorful, playful label. I'm very keen to see your ideas and I want something original.
Fermented foods and beverages

```html
<!DOCTYPE html>
<html lang="en">
<head>
<meta charset="utf-8">
<title>copper 71 kombucha labels</title>
<link rel="stylesheet" href="https://fonts.googleapis.com/css2?family=Alfa+Slab+One&family=Arimo:wght@400&display=swap">
<style>
  :root {
    --paper: #ffffff;
    --gold-deep: #d6b67a;
    --gold-light: #fbf2d6;
    --berry: #e1186f;
    --mango: #fac80f;
    --plum: #904af4;
    --ink-light: #ffffff;
  }
  html, body {
    margin: 0;
    padding: 0;
    width: 1200px;
    height: 515px;
    overflow: hidden;
    background: var(--paper);
  }
  .label-sheet { display: block; width: 1200px; height: 515px; }
  .gold-stop-deep { stop-color: var(--gold-deep); }
  .gold-stop-light { stop-color: var(--gold-light); }
  .label-gap { fill: var(--paper); }
  .label-band { fill: var(--paper); }
  .brand-circle { fill: none; stroke: var(--ink-light); stroke-width: 4; }
  .brand-name, .slogan, .ingredients, .product-note {
    font-family: 'Arimo', Arial, sans-serif;
    font-weight: 400;
    fill: var(--ink-light);
    text-anchor: middle;
  }
  .brand-name { font-size: 44px; }
  .brand-number { font-size: 30px; }
  .slogan { font-size: 18.5px; }
  .ingredients { font-size: 16.5px; }
  .product-note { font-size: 18.5px; }
  .product-title {
    font-family: 'Alfa Slab One', Georgia, serif;
    font-size: 49px;
    text-anchor: middle;
  }
  .label--berry .label-field { fill: var(--berry); }
  .label--berry .product-title { fill: var(--berry); }
  .label--mango .label-field { fill: var(--mango); }
  .label--mango .product-title { fill: var(--mango); }
  .label--plum .label-field { fill: var(--plum); }
  .label--plum .product-title { fill: var(--plum); }
</style>
</head>
<body>
<svg class="label-sheet" viewBox="0 0 1200 515" xmlns="http://www.w3.org/2000/svg">
  <defs>
    <linearGradient id="gold-rim" x1="0" y1="0" x2="1" y2="1">
      <stop offset="0" class="gold-stop-deep"/>
      <stop offset="0.25" class="gold-stop-light"/>
      <stop offset="0.5" class="gold-stop-deep"/>
      <stop offset="0.75" class="gold-stop-light"/>
      <stop offset="1" class="gold-stop-deep"/>
    </linearGradient>
    <clipPath id="field-shape">
      <ellipse cx="0" cy="257" rx="161" ry="211"/>
    </clipPath>
    <g id="label-body">
      <ellipse cx="0" cy="257" rx="196" ry="257" fill="url(#gold-rim)"/>
      <ellipse class="label-gap" cx="0" cy="257" rx="176" ry="236"/>
      <g clip-path="url(#field-shape)">
        <rect class="label-field" x="-170" y="40" width="340" height="440"/>
        <rect class="label-band" x="-170" y="232" width="340" height="71"/>
      </g>
    </g>
  </defs>

  <g class="label label--berry" transform="translate(196.5 0)">
    <use href="#label-body"/>
    <circle class="brand-circle" cx="0" cy="108" r="28"/>
    <text class="brand-name" x="0" y="184">copper</text>
    <text class="brand-name brand-number" x="0" y="219">71</text>
    <text class="product-title" x="0" y="288">kombucha</text>
    <text class="slogan" x="0" y="332">Dare to be Delicious</text>
    <text class="ingredients" x="0" y="382">Lorem ipsum ingredients</text>
    <text class="ingredients" x="0" y="402">Ingredients lorem</text>
    <text class="product-note" x="0" y="442">kombucha</text>
  </g>

  <g class="label label--mango" transform="translate(599.5 0)">
    <use href="#label-body"/>
    <circle class="brand-circle" cx="0" cy="108" r="28"/>
    <text class="brand-name" x="0" y="184">copper</text>
    <text class="brand-name brand-number" x="0" y="219">71</text>
    <text class="product-title" x="0" y="288">kombucha</text>
    <text class="slogan" x="0" y="332">Dare to be Delicious</text>
    <text class="ingredients" x="0" y="382">Lorem ipsum ingredients</text>
    <text class="ingredients" x="0" y="402">Ingredients lorem</text>
    <text class="product-note" x="0" y="442">kombucha</text>
  </g>

  <g class="label label--plum" transform="translate(1002.5 0)">
    <use href="#label-body"/>
    <circle class="brand-circle" cx="0" cy="108" r="28"/>
    <text class="brand-name" x="0" y="184">copper</text>
    <text class="brand-name brand-number" x="0" y="219">71</text>
    <text class="product-title" x="0" y="288">kombucha</text>
    <text class="slogan" x="0" y="332">Dare to be Delicious</text>
    <text class="ingredients" x="0" y="382">Lorem ipsum ingredients</text>
    <text class="ingredients" x="0" y="402">Ingredients lorem</text>
    <text class="product-note" x="0" y="442">kombucha</text>
  </g>
</svg>
</body>
</html>
```